IT Company needs stationary design

Business cards, MS Word, PowerPoint, A4 notepad design base on our company logo. This must be a set of templates in the same style which could be used both for printable documents as well as for documents shared digitally via email, website etc. This should be a modern design which is still professional, so make sure content is well readable both in MS Word and MS PowerPoint templates.
Updates

Target Market(s)

SME and Corporate

Industry/Entity Type

It Company

Font styles to use
Sans Serif

Colors
0455a3
0692cd
f37122
ffc214

Requirements
Must have
• 1) Business cards design: modern but still professional
• 2) MS Word: mostly for IT project documents (business analysis, reports, specifications, etc.) must be professional and easy readable.
• 3) MS PowerPoint: first slide, normal slide, last slide.
• 4) A4 notepad: header (must), footer (must), some light design on the background (optionally)
Nice to have
• Business cards design: would be nice to have 2-4 color variations of the same design from one side - cover (for example part of the cards are blue, part of the cards are orange) and other side with contact details is identical.

```html
<!DOCTYPE html>
<html lang="en">
<head>
<meta charset="utf-8">
<title>Corvane business cards</title>
<link rel="stylesheet" href="https://fonts.googleapis.com/css2?family=Open+Sans:wght@300;400;600&display=swap">
<style>
  :root {
    --backdrop: #3b3431;
    --card: #161719;
    --card-edge: #222326;
    --text-light: #eceef0;
    --text-muted: #8f9296;
    --brand-navy: #0455a3;
    --brand-blue: #0692cd;
    --brand-orange: #f37122;
    --brand-yellow: #ffc214;
    --divider: #8a8c90;
  }
  * { box-sizing: border-box; margin: 0; padding: 0; }
  html, body {
    width: 1200px; height: 864px; overflow: hidden;
    background: var(--backdrop);
    font-family: "Open Sans", Arial, sans-serif;
  }
  .sheet {
    width: 1200px; height: 864px;
    display: flex; flex-direction: column; align-items: center; justify-content: center; gap: 56px;
  }
  .card {
    position: relative; width: 600px; height: 343px;
    background: var(--card);
    border: 1px solid var(--card-edge);
    border-radius: 3px;
    box-shadow: 0 16px 34px rgba(0,0,0,.5);
  }
  .brand { display: flex; align-items: center; gap: 12px; }
  .brand__dot {
    width: 46px; height: 46px; border-radius: 50%;
    border: 3px solid var(--text-light);
    flex: none;
  }
  .brand__name {
    font-weight: 300; font-size: 42px; line-height: 1;
    color: var(--text-light);
  }

  /* Front */
  .card--front { display: flex; flex-direction: column; align-items: center; justify-content: center; }
  .card--front .brand { opacity: .72; }
  .front__url {
    margin-top: 40px; font-size: 14px; font-weight: 400;
    letter-spacing: 7px; color: var(--text-muted);
  }

  /* Back */
  .card--back { display: flex; align-items: center; }
  .back__brand { width: 318px; display: flex; justify-content: center; padding-left: 18px; }
  .back__brand .brand__dot { width: 42px; height: 42px; }
  .back__brand .brand__name { font-size: 38px; }
  .back__divider {
    align-self: stretch; width: 1px; margin: 56px 0;
    background: linear-gradient(to bottom, transparent, var(--divider) 20%, var(--divider) 80%, transparent);
  }
  .contact { padding-left: 20px; color: var(--text-light); }
  .contact__name {
    font-weight: 600; font-size: 18px; letter-spacing: .6px;
    color: var(--brand-blue); text-transform: uppercase; line-height: 1.15;
  }
  .contact__role {
    font-size: 13px; letter-spacing: .4px; color: var(--brand-orange);
    text-transform: uppercase; margin-bottom: 8px;
  }
  .contact__address { font-size: 14px; line-height: 1.35; margin-bottom: 3px; }
  .contact__list { list-style: none; font-size: 14px; line-height: 1.4; }
  .contact__list li { display: flex; align-items: center; gap: 9px; }
  .contact__icon { width: 12px; height: 12px; flex: none; }
</style>
</head>
<body>
<main class="sheet">
  <section class="card card--front" aria-label="Card front">
    <div class="brand">
      <span class="brand__dot"></span>
      <span class="brand__name">corvane</span>
    </div>
    <p class="front__url">www.corvane.com</p>
  </section>

  <section class="card card--back" aria-label="Card back">
    <div class="back__brand">
      <div class="brand">
        <span class="brand__dot"></span>
        <span class="brand__name">corvane</span>
      </div>
    </div>
    <div class="back__divider"></div>
    <div class="contact">
      <p class="contact__name">Alan Reyes</p>
      <p class="contact__role">President</p>
      <p class="contact__address">4120 Harbor Lane<br>Glen Ridge, NY 11020</p>
      <ul class="contact__list">
        <li>
          <svg class="contact__icon" viewBox="0 0 12 12" aria-hidden="true"><path fill="#0692cd" d="M1 3c0-1 1-2 2-2l1 2.5-1 1c.6 1.4 1.6 2.4 3 3l1-1L9.5 8c0 1-1 2-2 2C4 10 1 7 1 3z"/></svg>
          555 0142 7781
        </li>
        <li>
          <svg class="contact__icon" viewBox="0 0 12 12" aria-hidden="true"><rect x="3" y="0.5" width="6" height="11" rx="1.2" fill="#0692cd"/><rect x="4" y="2" width="4" height="7" fill="#161719"/></svg>
          555 0186 3409
        </li>
        <li>
          <svg class="contact__icon" viewBox="0 0 12 12" aria-hidden="true"><rect x="3" y="1" width="6" height="3" fill="#0692cd"/><rect x="1" y="4.5" width="10" height="5" rx="1" fill="#0692cd"/><rect x="3" y="8" width="6" height="3" fill="#0692cd" stroke="#161719" stroke-width=".8"/></svg>
          555 0127 6643
        </li>
        <li>
          <svg class="contact__icon" viewBox="0 0 12 12" aria-hidden="true"><rect x="0.5" y="2.5" width="11" height="7.5" rx="1" fill="#0692cd"/><path d="M1 3l5 4 5-4" fill="none" stroke="#161719" stroke-width="1"/></svg>
          alan@corvane.com
        </li>
        <li>
          <svg class="contact__icon" viewBox="0 0 12 12" aria-hidden="true"><circle cx="6" cy="6" r="5.3" fill="#0692cd"/><path d="M.8 6h10.4M6 .8c-2.4 2.8-2.4 7.6 0 10.4M6 .8c2.4 2.8 2.4 7.6 0 10.4" fill="none" stroke="#161719" stroke-width=".8"/></svg>
          www.corvane.com
        </li>
      </ul>
    </div>
  </section>
</main>
</body>
</html>
```